Business Card Project for Firm Deck Hoisting

Business name is "Firm Deck Hoisting" we are a scaffolding & rigging business specialising in local and remote work for:
- scaffolding (residential, commercial, industrial)
- rigging
-man material hoists
- swing stages
- labour hire

On the back of the card I would like FDH as the symbol / logo. I have attached the logos we have had created by sketch harbour. We would like to use bold colours – preferably as the same colour scheme as the logo.

Target Market(s)

Construction business

Industry/Entity Type

Construction

Contact Information for Business Card

name: Owen Pellew
Title: Director
Phone: 0491 572 864
Address: PO BOX 3251, Corlan Ridge SA 5990
Email: owen@firmdeckhoisting.com.au
Website: www.firmdeckhoisting.com.au

Font styles to use
Sans Serif

Requirements
Must have
• Must use existing logo & prefering using bold colours
Nice to have
• Would be nice to have a line of dot points in what we specialise in but not essential
• Would be nice to see some designs with a slogan but not essential
Should not have
• NA

```html
<!DOCTYPE html>
<html lang="en">
<head>
<meta charset="utf-8">
<title>Firm Deck Hoisting – Business Card</title>
<link rel="stylesheet" href="https://fonts.googleapis.com/css2?family=Montserrat:wght@400;500;600;700&display=swap">
<style>
  :root {
    --page: #e6e6e4;
    --white: #ffffff;
    --paper: #f3f4f5;
    --blue: #4f8fcf;
    --blue-light: #8dbbe6;
    --charcoal: #45494e;
    --charcoal-dark: #383b3f;
    --muted: #c9ccd0;
  }
  * { box-sizing: border-box; margin: 0; padding: 0; }
  html, body { width: 1200px; height: 900px; overflow: hidden; }
  body {
    background: var(--page);
    font-family: "Montserrat", Arial, sans-serif;
    display: flex;
    align-items: center;
    justify-content: center;
    gap: 40px;
  }
  .card {
    position: relative;
    width: 540px;
    height: 309px;
    border-radius: 4px;
    overflow: hidden;
    box-shadow: 0 6px 18px rgba(0,0,0,0.18);
  }
  .card-front { background: var(--white); }
  .card-front .shapes { position: absolute; inset: 0; }

  .brand {
    display: flex;
    align-items: center;
    gap: 10px;
    color: var(--charcoal);
    font-weight: 700;
    letter-spacing: 0.5px;
    white-space: nowrap;
  }
  .brand-mark {
    width: 16px; height: 16px;
    background: var(--blue);
    flex: none;
  }
  .card-front .brand {
    position: absolute;
    top: 44px; left: 36px;
    font-size: 22px;
  }

  .person {
    position: absolute;
    right: 34px;
    top: 150px;
    text-align: right;
    color: var(--white);
  }
  .person-name {
    font-size: 17px;
    font-weight: 600;
    letter-spacing: 1.5px;
    text-transform: uppercase;
  }
  .person-title {
    font-size: 10px;
    font-weight: 500;
    letter-spacing: 2px;
    text-transform: uppercase;
    opacity: 0.9;
    margin-top: 3px;
  }
  .contact-list {
    position: absolute;
    left: 300px;
    top: 204px;
    list-style: none;
    color: var(--white);
    font-size: 9.5px;
    font-weight: 500;
  }
  .contact-list li {
    display: flex;
    align-items: center;
    gap: 8px;
    height: 19px;
    white-space: nowrap;
  }
  .contact-list svg { width: 11px; height: 11px; flex: none; }

  .card-back {
    background:
      repeating-linear-gradient(45deg, rgba(255,255,255,0.025) 0 2px, transparent 2px 5px),
      linear-gradient(160deg, var(--charcoal), var(--charcoal-dark));
    display: flex;
    flex-direction: column;
    align-items: center;
    justify-content: center;
    gap: 14px;
  }
  .logo-plate {
    background: var(--white);
    padding: 16px 26px;
    border-radius: 2px;
  }
  .logo-plate .brand { font-size: 20px; }
  .back-web {
    color: var(--muted);
    font-size: 10px;
    letter-spacing: 1px;
  }
</style>
</head>
<body>

  <section class="card card-front">
    <svg class="shapes" viewBox="0 0 540 309" preserveAspectRatio="none">
      <polygon points="0,309 0,180 270,309" fill="var(--paper)"/>
      <polygon points="0,150 540,58 540,309 270,309 0,180" fill="var(--blue)"/>
      <polygon points="0,150 540,58 540,80 0,174" fill="var(--blue-light)"/>
      <polygon points="300,122 540,82 540,136 360,136" fill="var(--charcoal)"/>
    </svg>

    <div class="brand"><span class="brand-mark"></span>Firm Deck Hoisting</div>

    <div class="person">
      <p class="person-name">Owen Pellew</p>
      <p class="person-title">Director</p>
    </div>

    <ul class="contact-list">
      <li>
        <svg viewBox="0 0 12 12"><path d="M6 0.5a4 4 0 0 0-4 4c0 3 4 7 4 7s4-4 4-7a4 4 0 0 0-4-4zm0 5.6a1.6 1.6 0 1 1 0-3.2 1.6 1.6 0 0 1 0 3.2z" fill="#fff"/></svg>
        PO BOX 3251, Corlan Ridge SA 5990
      </li>
      <li>
        <svg viewBox="0 0 12 12"><path d="M2.5 0.8l2 0.2 1 2.6-1.3 1a6.5 6.5 0 0 0 3.2 3.2l1-1.3 2.6 1 0.2 2a1 1 0 0 1-1 1A9.8 9.8 0 0 1 1.5 1.8a1 1 0 0 1 1-1z" fill="#fff"/></svg>
        0491 572 864
      </li>
      <li>
        <svg viewBox="0 0 12 12"><rect x="0.5" y="2.2" width="11" height="7.6" rx="1" fill="#fff"/><path d="M1 2.8l5 3.8 5-3.8" stroke="var(--blue)" stroke-width="1" fill="none"/></svg>
        owen@firmdeckhoisting.com.au
      </li>
      <li>
        <svg viewBox="0 0 12 12"><circle cx="6" cy="6" r="5" stroke="#fff" stroke-width="1.1" fill="none"/><ellipse cx="6" cy="6" rx="2.2" ry="5" stroke="#fff" stroke-width="1" fill="none"/><path d="M1 6h10" stroke="#fff" stroke-width="1"/></svg>
        www.firmdeckhoisting.com.au
      </li>
    </ul>
  </section>

  <section class="card card-back">
    <div class="logo-plate">
      <div class="brand"><span class="brand-mark"></span>Firm Deck Hoisting</div>
    </div>
    <p class="back-web">www.firmdeckhoisting.com.au</p>
  </section>

</body>
</html>
```